Packaging Design New Cosmetics Range

Small Establish online Beauty company is expanding it's product range into Serums, Sprays and Creams . We are looking for a new fresh packaging design for this launch.
We only use products that are Organic , Not Tested on Animals and Natural products
We would be interested in viewing a White Design , Black design and a designer choice of colors .
First Products are
Rose Water in 100ml glass bottle with box
and a set of 3 Face Serums Vit C , Retinol and Hyaluronic in 30ml Glass bottle = Box
Scrubs and creams will launch later in Q1 2020 however would like a similar feel across all products
Target Market(s)
SEA / US Markets
Industry/Entity Type
Cosmetics
Colors
Designer to choose colors to be used in the design.
Requirements
Must have
- Space Allocated for Product Use and Bar Codes on Box
Nice to have
- Organic , Not tested on animal Logo's

```html
<!DOCTYPE html>
<html lang="en">
<head>
<meta charset="UTF-8">
<title>Organic Retinol Face Serum – Packaging</title>
<link rel="stylesheet" href="https://fonts.googleapis.com/css2?family=Bebas+Neue&family=Josefin+Sans:wght@400;700&family=Kaushan+Script&display=swap">
<style>
  :root {
    --backdrop: #e3e7e7;
    --white: #ffffff;
    --black: #0e0e0e;
    --purple: #a94fa4;
    --purple-soft: #c98fc6;
    --grey: #c8c8c8;
    --grey-dark: #4a4a4a;
    --teal: #2aa58c;
    --ink: #1a1a1a;
  }
  * { box-sizing: border-box; margin: 0; padding: 0; }
  html, body { width: 1200px; height: 901px; overflow: hidden; background: var(--backdrop); }
  .stage { position: relative; width: 1200px; height: 901px; background: var(--backdrop); }

  .panel { position: absolute; overflow: hidden; text-align: center; }
  .panel--white { background: var(--white); color: var(--ink); box-shadow: 0 4px 14px rgba(0,0,0,.12); }
  .panel--black { background: var(--black); color: var(--white); box-shadow: 0 4px 14px rgba(0,0,0,.25); }

  .box { top: 19px; width: 252px; height: 755px; }
  .box--white { left: 326px; }
  .box--black { left: 618px; }
  .label { top: 440px; width: 186px; height: 335px; }
  .label--white { left: 122px; }
  .label--black { left: 896px; }

  .top-band { position: absolute; left: 0; right: 0; top: 0; background: var(--purple); }
  .box .top-band { height: 30px; }
  .label .top-band { height: 18px; }

  .brand {
    position: absolute; left: 0; right: 0;
    font-family: "Josefin Sans", sans-serif; font-weight: 400;
    color: var(--teal); display: flex; align-items: center; justify-content: center; gap: 7px;
  }
  .brand__dot { display: inline-block; border-radius: 50%; background: var(--teal); }
  .box .brand { top: 150px; font-size: 30px; }
  .box .brand__dot { width: 12px; height: 12px; }
  .label .brand { top: auto; bottom: 14px; left: auto; right: 12px; font-size: 17px; gap: 4px; }
  .label .brand__dot { width: 7px; height: 7px; }

  .product-title { position: absolute; left: 0; right: 0; }
  .product-title__organic { display: block; font-family: "Kaushan Script", cursive; color: #555; }
  .panel--black .product-title__organic { color: #d8d8d8; }
  .product-title__name { display: block; font-family: "Bebas Neue", sans-serif; letter-spacing: 2px; }
  .product-title__type { display: block; font-family: "Josefin Sans", sans-serif; letter-spacing: 4px; }
  .box .product-title { top: 262px; }
  .box .product-title__organic { font-size: 34px; line-height: 1; }
  .box .product-title__name { font-size: 64px; line-height: .95; }
  .box .product-title__type { font-size: 21px; }
  .label .product-title { top: 40px; }
  .panel--black.label .product-title { top: 48px; }
  .label .product-title__organic { font-size: 24px; line-height: 1; }
  .label .product-title__name { font-size: 42px; line-height: .95; }
  .label .product-title__type { font-size: 15px; letter-spacing: 3px; }

  .vitamin {
    position: absolute; left: 50%; transform: translateX(-50%); z-index: 2;
    border-radius: 50%; background: var(--purple); color: var(--white);
    font-family: "Josefin Sans", sans-serif; font-weight: 700;
    display: flex; align-items: center; justify-content: center;
  }
  .box .vitamin { top: 398px; width: 60px; height: 60px; font-size: 38px; padding-top: 5px; }
  .label .vitamin { top: 166px; width: 44px; height: 44px; font-size: 28px; padding-top: 4px; }
  .panel--black.label .vitamin { top: 174px; }

  .ornament { position: absolute; left: 0; right: 0; z-index: 1; }
  .box--white .ornament { top: 505px; height: 205px; background: linear-gradient(180deg, #ffffff 0%, #e6d2e5 35%, var(--grey) 70%, var(--purple-soft) 100%); }
  .box--black .ornament { top: 472px; height: 238px; background: linear-gradient(160deg, var(--purple) 0%, var(--grey-dark) 45%, #1e1e1e 100%); }
  .label--white .ornament { top: 218px; height: 72px; background: linear-gradient(180deg, #ffffff 0%, #e6d2e5 40%, var(--grey) 100%); }
  .label--black .ornament { top: 222px; height: 68px; background: linear-gradient(160deg, var(--purple) 0%, var(--grey-dark) 60%, #1e1e1e 100%); }

  .volume { position: absolute; z-index: 2; font-family: "Josefin Sans", sans-serif; font-weight: 700; font-size: 16px; }
  .box--white .volume { top: 690px; left: 0; right: 0; }
  .box--black .volume { bottom: 26px; left: 12px; color: var(--white); }

  .badge { position: absolute; border: 2px solid currentColor; border-radius: 3px; }
  .box .badge { bottom: 16px; right: 12px; width: 88px; height: 26px; }
  .label .badge { bottom: 14px; left: 12px; width: 62px; height: 20px; }
  .panel--white .badge { color: var(--ink); }
  .panel--black .badge { color: var(--white); }
</style>
</head>
<body>
<main class="stage">

  <section class="panel panel--white label label--white" aria-label="Bottle label, white edition">
    <h2 class="product-title">
      <span class="product-title__organic">Organic</span>
      <span class="product-title__name">RETINOL</span>
      <span class="product-title__type">FACE SERUM</span>
    </h2>
    <div class="vitamin">A</div>
    <div class="ornament" role="img" aria-label="Purple and grey lotus drop ornament"></div>
    <div class="badge" aria-label="Cruelty-free badge"></div>
    <div class="brand"><span class="brand__dot"></span>Velora</div>
  </section>

  <section class="panel panel--white box box--white" aria-label="Box front, white edition">
    <div class="brand"><span class="brand__dot"></span>Velora</div>
    <h2 class="product-title">
      <span class="product-title__organic">Organic</span>
      <span class="product-title__name">RETINOL</span>
      <span class="product-title__type">FACE SERUM</span>
    </h2>
    <div class="vitamin">A</div>
    <div class="ornament" role="img" aria-label="Large purple and grey lotus drop ornament"></div>
    <div class="volume">30ml</div>
    <div class="badge" aria-label="Cruelty-free badge"></div>
  </section>

  <section class="panel panel--black box box--black" aria-label="Box front, black edition">
    <div class="top-band"></div>
    <div class="brand"><span class="brand__dot"></span>Velora</div>
    <h2 class="product-title">
      <span class="product-title__organic">Organic</span>
      <span class="product-title__name">RETINOL</span>
      <span class="product-title__type">FACE SERUM</span>
    </h2>
    <div class="vitamin">A</div>
    <div class="ornament" role="img" aria-label="Large purple and grey lotus petal ornament"></div>
    <div class="volume">30ml</div>
    <div class="badge" aria-label="Cruelty-free badge"></div>
  </section>

  <section class="panel panel--black label label--black" aria-label="Bottle label, black edition">
    <div class="top-band"></div>
    <h2 class="product-title">
      <span class="product-title__organic">Organic</span>
      <span class="product-title__name">RETINOL</span>
      <span class="product-title__type">FACE SERUM</span>
    </h2>
    <div class="vitamin">A</div>
    <div class="ornament" role="img" aria-label="Purple and grey lotus petal ornament"></div>
    <div class="badge" aria-label="Cruelty-free badge"></div>
    <div class="brand"><span class="brand__dot"></span>Velora</div>
  </section>

</main>
</body>
</html>
```